Professional Oral Surgery Referral Pad, Business Card, and Stationary Design

Hello,

I want to work with a designer for my startup Oral Surgery Practice called: Dorrel Creek Oral Surgery & Implant Center

Ideally I would like to choose a good/professional design and work with a designer all the way to fulfill ALL of our stationary needs including referral pads, business cards, letterheads, envelopes, notepads, email signature, etc.

I would like to see designs first and hopefully would like to work with the designer for the lifetime of my practice and wanting to develop a long-term professional relationship.

In terms of the logo I have attached our practice logo files: I want to stay within the 3 colorways of the logo: Navy Blue/Silver grey/White. I would like for you to be creative and incorporate the "V" as best you can (for example greyed out watermark, etc)

I have also attached in my files the full contact info of our office in a word document: which includes address, email address, phone, fax, cell, etc.

I have also attached a few examples of double sided referral pad we can draw inspiration from. In terms of the referral pad I would ideally like to have my logo nicely placed/incorporated to make it look professional, address of the practice and contact info, my name and credentials.

Referral pad must have lines for patient, date of birth, phone number, referring doctor name, odontogram of all adult teeth and pediatric teeth, nice and big - so easy for dentist to refer. Also a jaw drawing of the intraoral cavity. Below that should have comments to surgeon.

In terms of procedures, I would like to have options of IV sedation, extractions, wisdom teeth, bone graft, pathology, tmj, trauma, expose/bond, orthognathic, other (list below)

In the back we can have a greyed out map of my practice address and Instructions for patients should include to bring insurance documentation, medication list, etc.

The final nitty gritty details of the referral pad can be worked on once I am happy with the design.

Target Market(s)

Patients who need oral surgical services and dentist referrals

Industry/Entity Type

Oral and Maxillofacial Surgery

• I would leave it up to the designers!

Colors
0054AA
0677BA
7BADD7
CADEEF
E8F1F8

Requirements
Must have
• Professional/sleek/modern and three color ways same as logo (navy blue, silver gray, and white)
Nice to have
• I would like to highlight my logo especially the implant ā€œvā€ either as watermark or part of the header or footnote. I will leave it to the expertise of the designer

```html
<!DOCTYPE html>
<html lang="en">
<head>
<meta charset="utf-8">
<title>Dorrel Creek Oral Surgery &amp; Implant Center — Stationery</title>
<link href="https://fonts.googleapis.com/css2?family=Montserrat:wght@400;600;700&family=Raleway:wght@300;400&display=swap" rel="stylesheet">
<style>
  :root{
    --navy:#0b3b8f;
    --navy-soft:#15479b;
    --silver:#9aa0a8;
    --silver-light:#dfe4ec;
    --ink:#5c6470;
    --paper:#ffffff;
    --backdrop:#cecece;
    --line:#c9ced6;
  }
  *{box-sizing:border-box;margin:0;padding:0}
  html,body{width:1200px;height:714px;overflow:hidden;background:var(--backdrop)}
  body{position:relative;font-family:"Montserrat",sans-serif;color:var(--ink)}
  .piece{position:absolute;background:var(--paper);box-shadow:0 2px 5px rgba(0,0,0,.22);overflow:hidden}
  .piece.navy{background:var(--navy)}
  .brand{position:absolute;display:flex;align-items:center;gap:5px;font-family:"Montserrat",sans-serif;font-weight:600;color:var(--navy);line-height:1.15}
  .brand .mark{flex:none;background:var(--navy)}
  .brand.light{color:#fff}
  .brand.light .mark{background:#fff}
  .doctor{position:absolute;font-weight:700;color:var(--navy);letter-spacing:.2px}
  .doctor small{display:block;font-weight:400;color:var(--ink);letter-spacing:0}
  .contacts{position:absolute;font-family:"Raleway",sans-serif;color:var(--ink);line-height:1.9}
  .contacts .row{display:flex;align-items:center;gap:3px}
  .contacts svg{fill:var(--navy);flex:none}
  .rule{position:absolute;height:1px;background:var(--navy)}
  .emblem{position:absolute;border-radius:50%;background:var(--silver-light)}
  .lorem{font-family:"Raleway",sans-serif;font-weight:300;color:#7a808a;text-align:justify}
</style>
</head>
<body>
<svg width="0" height="0" style="position:absolute">
  <defs>
    <symbol id="i-phone" viewBox="0 0 10 10"><path d="M2 0h2l1 2.5-1.3 1a5 5 0 0 0 2.8 2.8l1-1.3L10 6v2a2 2 0 0 1-2 2A8 8 0 0 1 0 2a2 2 0 0 1 2-2z"/></symbol>
    <symbol id="i-fax" viewBox="0 0 10 10"><path d="M2 0h6v3H2zM0 3.5h10V9H0zM2.5 6h5v4h-5z" fill-rule="evenodd"/></symbol>
    <symbol id="i-mail" viewBox="0 0 10 10"><path d="M0 2h10v6H0zM0 2l5 3.5L10 2" stroke="#fff" stroke-width=".8"/></symbol>
    <symbol id="i-pin" viewBox="0 0 10 10"><path d="M5 0a3.6 3.6 0 0 1 3.6 3.6C8.6 6.2 5 10 5 10S1.4 6.2 1.4 3.6A3.6 3.6 0 0 1 5 0zm0 2.2a1.4 1.4 0 1 0 0 2.8 1.4 1.4 0 0 0 0-2.8z"/></symbol>
  </defs>
</svg>

<!-- Master lockup -->
<div class="brand" style="left:170px;top:42px;font-size:11px">
  <span class="mark" style="width:12px;height:12px"></span>
  <span>Dorrel Creek Oral Surgery<br>&amp; Implant Center</span>
</div>

<!-- Business card, front -->
<section class="piece business-card" style="left:38px;top:95px;width:202px;height:121px">
  <div class="brand" style="left:13px;top:16px;font-size:6.5px">
    <span class="mark" style="width:8px;height:8px"></span>
    <span>Dorrel Creek Oral Surgery<br>&amp; Implant Center</span>
  </div>
  <div class="doctor" style="left:14px;top:62px;font-size:7px">DR. ANIL VARMA, DDS<small style="font-size:3.8px;margin-top:1px">Dorrel Creek Oral Surgery &amp; Implant Center</small></div>
  <div class="contacts" style="left:14px;top:82px;font-size:3.9px">
    <div class="row"><svg width="4" height="4"><use href="#i-phone"/></svg>555 014 2281&nbsp;&nbsp;<svg width="4" height="4"><use href="#i-fax"/></svg>555 014 2290</div>
    <div class="row"><svg width="4" height="4"><use href="#i-mail"/></svg>info@dorrelcreekoms.com</div>
    <div class="row"><svg width="4" height="4"><use href="#i-pin"/></svg>18 Alder Row, Dorrel Creek, CA 90000</div>
  </div>
  <div class="emblem" style="left:132px;top:52px;width:56px;height:56px"></div>
  <div class="rule" style="left:0;right:0;top:109px"></div>
</section>

<!-- Business card, back -->
<section class="piece navy business-card-back" style="left:262px;top:95px;width:202px;height:121px">
  <div class="brand light" style="left:39px;top:50px;font-size:8.5px">
    <span class="mark" style="width:10px;height:10px"></span>
    <span>Dorrel Creek Oral Surgery<br>&amp; Implant Center</span>
  </div>
</section>

<!-- Compliment slip -->
<section class="piece compliment-slip" style="left:38px;top:250px;width:358px;height:90px">
  <div class="brand" style="left:14px;top:13px;font-size:6px">
    <span class="mark" style="width:8px;height:8px"></span>
    <span>Dorrel Creek Oral Surgery<br>&amp; Implant Center</span>
  </div>
  <div class="doctor" style="left:14px;top:38px;font-size:6.5px">DR. ANIL VARMA, DDS<small style="font-size:3.6px;margin-top:1px">Dorrel Creek Oral Surgery &amp; Implant Center</small></div>
  <div class="contacts" style="left:14px;top:59px;font-size:3.7px;line-height:2">
    <div class="row"><svg width="4" height="4"><use href="#i-phone"/></svg>555 014 2281&nbsp;&nbsp;<svg width="4" height="4"><use href="#i-fax"/></svg>555 014 2290</div>
    <div class="row"><svg width="4" height="4"><use href="#i-mail"/></svg>info@dorrelcreekoms.com</div>
    <div class="row"><svg width="4" height="4"><use href="#i-pin"/></svg>18 Alder Row, Dorrel Creek, CA 90000</div>
  </div>
  <div class="emblem" style="left:282px;top:38px;width:46px;height:46px"></div>
  <div class="rule" style="left:0;right:0;top:82px"></div>
</section>

<!-- Letterhead with navy second sheet -->
<div class="piece navy letterhead-second" style="left:520px;top:65px;width:259px;height:363px"></div>
<section class="piece letterhead" style="left:498px;top:87px;width:259px;height:363px">
  <div class="brand" style="left:21px;top:22px;font-size:7px">
    <span class="mark" style="width:9px;height:9px"></span>
    <span>Dorrel Creek Oral Surgery<br>&amp; Implant Center</span>
  </div>
  <div class="recipient" style="position:absolute;left:21px;top:77px;font-family:Raleway,sans-serif;font-size:4.4px;line-height:1.7;color:#8a909a">
    <div style="font-family:Montserrat,sans-serif;font-weight:600;font-size:7.5px;color:var(--navy);margin-bottom:2px">Lena Marsh</div>
    0123-456-789<br>info@youremailaddress.com<br><span style="display:block;margin-top:1px">1234 Harbor Ln. Suite<br>12 Brookfield, TX 0000</span>
  </div>
  <div style="position:absolute;right:21px;top:127px;font-family:Raleway,sans-serif;font-size:5px;color:#7a808a">12 December, 2024</div>
  <div class="lorem" style="position:absolute;left:21px;right:21px;top:138px;font-size:5px;line-height:7.8px">
    <p>Lorem ipsum dolor sit amet, consectetuer adipiscing elit, sed diam nonummy nibh euismod tincidunt ut laoreet dolore magna aliquam erat volutpat. Ut wisi enim ad minim veniam, quis nostrud exerci tation ullamcorper suscipit lobortis nisl ut aliquip ex ea commodo consequat. Duis autem vel eum iriure dolor in hendrerit in vulputate velit esse molestie consequat, vel illum dolore eu feugiat nulla facilisis at vero eros et accumsan et iusto odio dignissim qui blandit praesent luptatum zzril delenit augue duis dolore te feugait nulla facilisi.</p>
    <p style="margin-top:7.8px">Lorem ipsum dolor sit amet, cons ectetuer adipiscing elit, sed diam nonummy nibh euismod tincidunt ut laoreet dolore magna aliquam erat volutpat. Ut wisi enim ad minim veniam, quis nostrud exerci tation ullamcorper suscipit lobortis nisl ut aliquip ex ea commodo consequat.</p>
  </div>
  <div style="position:absolute;right:21px;top:250px;font-size:5.8px;font-weight:600;color:#4a505a">Mr. Owen T. Hale</div>
  <div role="img" aria-label="Handwritten signature" style="position:absolute;left:186px;top:262px;width:40px;height:22px;background:#eef0f3"></div>
  <div class="contacts" style="left:11px;top:327px;font-size:3.8px;line-height:2">
    <div class="row"><svg width="4" height="4"><use href="#i-phone"/></svg>555 014 2281&nbsp;&nbsp;<svg width="4" height="4"><use href="#i-fax"/></svg>555 014 2290</div>
    <div class="row"><svg width="4" height="4"><use href="#i-mail"/></svg>info@dorrelcreekoms.com</div>
    <div class="row"><svg width="4" height="4"><use href="#i-pin"/></svg>18 Alder Row, Dorrel Creek, CA 90000</div>
  </div>
  <div class="emblem" style="left:196px;top:314px;width:38px;height:38px"></div>
  <div class="rule" style="left:0;right:0;top:350px"></div>
</section>

<!-- Notepad cover -->
<section class="piece navy notepad-cover" style="left:811px;top:82px;width:152px;height:212px;border-radius:6px">
  <div class="brand light" style="left:24px;top:100px;font-size:6.5px">
    <span class="mark" style="width:8px;height:8px"></span>
    <span>Dorrel Creek Oral Surgery<br>&amp; Implant Center</span>
  </div>
</section>

<!-- Notepad page -->
<section class="piece notepad-page" style="left:982px;top:82px;width:152px;height:212px;border-radius:6px">
  <div class="brand" style="left:13px;top:14px;font-size:3.4px">
    <span class="mark" style="width:5px;height:5px"></span>
    <span>Dorrel Creek Oral Surgery<br>&amp; Implant Center</span>
  </div>
  <div style="position:absolute;left:102px;top:16px;font-size:3.2px;color:#666">Date: __/__/____</div>
  <svg style="position:absolute;left:12px;top:30px" width="130" height="180" aria-hidden="true">
    <g stroke="#c6cbd2" stroke-width=".5">
      <line x1="0" y1="1" x2="130" y2="1"/><line x1="0" y1="13" x2="130" y2="13"/><line x1="0" y1="25" x2="130" y2="25"/><line x1="0" y1="37" x2="130" y2="37"/><line x1="0" y1="49" x2="130" y2="49"/><line x1="0" y1="61" x2="130" y2="61"/><line x1="0" y1="73" x2="130" y2="73"/><line x1="0" y1="85" x2="130" y2="85"/><line x1="0" y1="97" x2="130" y2="97"/><line x1="0" y1="109" x2="130" y2="109"/><line x1="0" y1="121" x2="130" y2="121"/><line x1="0" y1="133" x2="130" y2="133"/><line x1="0" y1="145" x2="130" y2="145"/><line x1="0" y1="157" x2="130" y2="157"/><line x1="0" y1="169" x2="130" y2="169"/>
    </g>
  </svg>
  <div class="emblem" style="left:105px;top:168px;width:30px;height:30px;opacity:.6"></div>
</section>

<!-- Envelope, back with flap -->
<section class="piece envelope-back" style="left:802px;top:318px;width:337px;height:170px">
  <svg style="position:absolute;left:0;top:0" width="337" height="42" aria-hidden="true">
    <path d="M0 0H337L325 30Q320 41 306 41H31Q17 41 12 30Z" fill="var(--navy)"/>
  </svg>
  <div class="brand light" style="left:124px;top:14px;font-size:5.5px">
    <span class="mark" style="width:7px;height:7px"></span>
    <span>Dorrel Creek Oral Surgery<br>&amp; Implant Center</span>
  </div>
</section>

<!-- Envelope, front -->
<section class="piece envelope-front" style="left:802px;top:507px;width:337px;height:169px">
  <div class="brand" style="left:11px;top:13px;font-size:5.3px">
    <span class="mark" style="width:7px;height:7px"></span>
    <span>Dorrel Creek Oral Surgery<br>&amp; Implant Center</span>
  </div>
  <div style="position:absolute;left:11px;top:32px;font-family:Raleway,sans-serif;font-size:4.6px;line-height:1.35;color:#6a707a">18 Alder Row<br>Dorrel Creek, CA 90000</div>
  <div class="emblem" style="left:255px;top:112px;width:46px;height:46px"></div>
  <div class="rule" style="left:0;right:0;top:157px"></div>
</section>

<!-- Notebook cover -->
<section class="piece navy notebook-cover" style="left:47px;top:388px;width:203px;height:287px">
  <div class="emblem" style="left:52px;top:40px;width:100px;height:100px;background:var(--navy-soft)"></div>
  <div class="emblem" style="left:52px;top:168px;width:100px;height:100px;background:var(--navy-soft)"></div>
  <div class="brand light" style="left:34px;top:132px;font-size:8.5px">
    <span class="mark" style="width:10px;height:10px"></span>
    <span>Dorrel Creek Oral Surgery<br>&amp; Implant Center</span>
  </div>
</section>

<!-- Referral pad -->
<section class="piece referral-pad" style="left:270px;top:388px;width:201px;height:287px">
  <div class="brand" style="left:14px;top:17px;font-size:4.8px">
    <span class="mark" style="width:7px;height:7px"></span>
    <span>Dorrel Creek Oral Surgery<br>&amp; Implant Center</span>
  </div>
  <div class="doctor" style="left:130px;top:7px;font-size:4.6px">DR. ANIL VARMA, DDS<small style="font-size:2.4px">Dorrel Creek Oral Surgery &amp; Implant Center</small></div>
  <div class="contacts" style="left:130px;top:23px;font-size:2.4px;line-height:2.1">
    <div class="row"><svg width="3" height="3"><use href="#i-phone"/></svg>555 014 2281 <svg width="3" height="3"><use href="#i-fax"/></svg>555 014 2290</div>
    <div class="row"><svg width="3" height="3"><use href="#i-mail"/></svg>info@dorrelcreekoms.com</div>
    <div class="row"><svg width="3" height="3"><use href="#i-pin"/></svg>18 Alder Row, Dorrel Creek, CA 90000</div>
  </div>
  <div class="rule" style="left:0;right:0;top:38px"></div>

  <svg style="position:absolute;left:12px;top:44px" width="178" height="56" aria-hidden="true">
    <g font-family="Montserrat,sans-serif" font-size="3.6" fill="var(--navy)">
      <text x="0" y="8">Patient:</text>
      <text x="0" y="22">Date of Birth:</text><text x="90" y="22">Patient Phone:</text>
      <text x="0" y="35">Referred By Dr.:</text>
      <text x="5" y="46">Call to appoint</text><text x="50" y="46">Patient will call</text><text x="103" y="46">Appointment made by referring doctor</text>
    </g>
    <g stroke="#b3b9c2" stroke-width=".4" stroke-dasharray="1 1">
      <line x1="15" y1="8" x2="178" y2="8"/><line x1="25" y1="22" x2="88" y2="22"/><line x1="117" y1="22" x2="178" y2="22"/><line x1="30" y1="35" x2="178" y2="35"/>
    </g>
    <g fill="none" stroke="var(--navy)" stroke-width=".4">
      <rect x="0.5" y="43" width="3" height="3"/><rect x="45.5" y="43" width="3" height="3"/><rect x="98.5" y="43" width="3" height="3"/>
    </g>
  </svg>

  <div role="img" aria-label="Jaw drawing and odontogram of adult and pediatric teeth" style="position:absolute;left:12px;top:104px;width:120px;height:66px;background:linear-gradient(#f3f4f6,#e7e9ec)"></div>

  <svg style="position:absolute;left:135px;top:101px" width="56" height="72" aria-hidden="true">
    <rect x=".3" y=".3" width="55.4" height="71.4" fill="none" stroke="#c3c8cf" stroke-width=".5" stroke-dasharray="1 1"/>
    <text x="4" y="8" font-family="Montserrat,sans-serif" font-weight="600" font-size="3.6" fill="var(--navy)">Select Indication(s):</text>
    <g font-family="Raleway,sans-serif" font-size="3.5" fill="#8a909a">
      <text x="8" y="17">extraction(s)</text><text x="8" y="23.4">wisdom teeth</text><text x="8" y="29.8">dental implant</text><text x="8" y="36.2">pathology</text><text x="8" y="42.6">tmj</text><text x="8" y="49">trauma</text><text x="8" y="55.4">expose &amp; bond</text><text x="8" y="61.8">facial cosmetic</text><text x="8" y="68.2">other (list below)</text>
    </g>
    <g fill="none" stroke="#8a909a" stroke-width=".35">
      <rect x="3.5" y="14.3" width="3" height="3"/><rect x="3.5" y="20.7" width="3" height="3"/><rect x="3.5" y="27.1" width="3" height="3"/><rect x="3.5" y="33.5" width="3" height="3"/><rect x="3.5" y="39.9" width="3" height="3"/><rect x="3.5" y="46.3" width="3" height="3"/><rect x="3.5" y="52.7" width="3" height="3"/><rect x="3.5" y="59.1" width="3" height="3"/><rect x="3.5" y="65.5" width="3" height="3"/>
    </g>
  </svg>

  <svg style="position:absolute;left:12px;top:178px" width="178" height="28" aria-hidden="true">
    <rect x=".3" y=".3" width="177.4" height="27.4" rx="4" fill="none" stroke="var(--navy)" stroke-width=".5"/>
    <text x="3.5" y="7" font-family="Montserrat,sans-serif" font-weight="600" font-size="3.6" fill="var(--navy)">Comments to Surgeon:</text>
    <g stroke="#c3c8cf" stroke-width=".35" stroke-dasharray="1 1"><line x1="3" y1="13" x2="175" y2="13"/><line x1="3" y1="19" x2="175" y2="19"/><line x1="3" y1="25" x2="175" y2="25"/></g>
  </svg>

  <svg style="position:absolute;left:12px;top:208px" width="178" height="40" aria-hidden="true">
    <g fill="var(--navy)"><circle cx="36" cy="3" r=".8"/><circle cx="38.5" cy="3" r=".8"/><circle cx="41.5" cy="3" r="1.4"/><circle cx="139" cy="3" r="1.4"/><circle cx="142" cy="3" r=".8"/><circle cx="144.5" cy="3" r=".8"/></g>
    <g stroke="var(--navy)" stroke-width=".4"><line x1="43" y1="3" x2="52" y2="3"/><line x1="127" y1="3" x2="137.5" y2="3"/></g>
    <text x="89" y="4.3" text-anchor="middle" font-family="Montserrat,sans-serif" font-weight="600" font-size="3.6" fill="var(--navy)">INSTRUCTIONS TO PATIENTS:</text>
    <g font-family="Raleway,sans-serif" font-size="3.5" fill="#7a808a">
      <text x="0" y="15">1. Your appointment is on</text><text x="140" y="15">at</text>
      <text x="0" y="23.5">2. Please bring <tspan fill="var(--navy)" font-weight="400" font-family="Montserrat,sans-serif">MEDICAL and DENTAL</tspan> insurance information with you</text>
      <text x="0" y="32">3. Visit <tspan fill="var(--navy)" font-family="Montserrat,sans-serif">www.DORRELCREEKOMS.com</tspan> to register prior to appt.</text>
    </g>
    <g stroke="#b3b9c2" stroke-width=".35" stroke-dasharray="1 1"><line x1="48" y1="15" x2="138" y2="15"/><line x1="145" y1="15" x2="178" y2="15"/></g>
  </svg>

  <div class="emblem" style="left:151px;top:222px;width:40px;height:40px"></div>
  <svg style="position:absolute;left:0;top:247px" width="201" height="32" aria-hidden="true">
    <path d="M0 0H175L201 -10V32H0Z" fill="var(--navy)"/>
  </svg>
  <div style="position:absolute;left:12px;top:251px;width:150px;font-size:4.3px;font-weight:700;line-height:1.45;color:#fff">Do not eat or drink anything (even water) 6 hrs prior to appointment if you are having surgery that day.<br>An adult driver must accompany you and remain present if you are having surgery.</div>
</section>
</body>
</html>
```